We need a tri fold brochure for a new private investigator based in Modesto CA called Brenwick Inquiry Partners. We rely heavily on technology and bring a new level of efficiency to the investigative industry.

We primarily serve individual attorneys and law firms with pre and post litigation support. We bring a higher level of professionalism and technology to our clients and plan on raining the bar of service provider expectation.

Target Market(s)

Attorneys and legal support staff

Industry/Entity Type

Private Investigator

Requirements
Must have
• I must have my logo and contact information, must only use the colors of red, white and black
Nice to have
• I would like a very clean and simple design, these are going to attorneys and legal support staff who need to be able to look at and and understand the tri-fold quickly and easily, but look very up-scale and sophisticated

```html
<!DOCTYPE html>
<html lang="en">
<head>
<meta charset="utf-8">
<title>Brenwick Inquiry Partners – Services Brochure</title>
<link href="https://fonts.googleapis.com/css2?family=Jost:wght@400;500&display=swap" rel="stylesheet">
<style>
  :root {
    --red: #ed1c24;
    --white: #ffffff;
    --ink: #231f20;
    --grey-light: #e6e6e6;
    --grey-mid: #cfcfcf;
    --grey-deep: #b8b8b8;
    --page: #ffffff;
  }
  * { box-sizing: border-box; margin: 0; padding: 0; }
  html, body { width: 1200px; height: 933px; overflow: hidden; background: var(--page); }
  body { font-family: "Jost", "Futura", sans-serif; color: var(--ink); }

  .brochure {
    position: absolute; left: 60px; top: 85px;
    width: 1080px; height: 762px;
    display: flex;
  }
  .panel { position: relative; width: 360px; height: 100%; }
  .panel--left   { background: linear-gradient(to bottom, var(--white) 0%, var(--white) 42%, var(--grey-mid) 100%); }
  .panel--middle { background: linear-gradient(to bottom, var(--grey-light) 0%, var(--white) 32%, var(--white) 100%); }
  .panel--right  { background: linear-gradient(to bottom, var(--white) 0%, var(--white) 40%, var(--grey-deep) 100%); }

  .section { position: absolute; left: 0; width: 360px; }
  .section__title {
    background: var(--red); color: var(--white);
    font-weight: 500; font-size: 16px; letter-spacing: 0.2px;
    text-transform: uppercase;
    height: 25px; line-height: 26px;
    padding-left: 39px;
  }
  .section__body {
    margin: 15px 39px 0 39px;
    font-size: 11px; line-height: 16px; letter-spacing: 0.25px;
    text-align: justify;
    hyphens: auto; -webkit-hyphens: auto;
  }
  .services { margin: 32px 39px 0 39px; list-style: none; font-size: 11px; line-height: 16px; letter-spacing: 0.25px; }
  .services li { position: relative; padding-left: 15px; margin-bottom: 16px; }
  .services li::before {
    content: ""; position: absolute; left: 2px; top: 6px;
    width: 4px; height: 4px; border-radius: 50%; background: var(--ink);
  }
</style>
</head>
<body>
<main class="brochure">
  <section class="panel panel--left">
    <div class="section" style="top:116px">
      <h2 class="section__title">Statements</h2>
      <p class="section__body">Taking statements is a unique skill developed over many years of interviewing subjects. A recent FBI study revealed that most unsuccessful interviews are the result of the interviewer not asking the right questions. We have logged hundreds of hours conducting recorded statements and we ask the right questions. We consult with you, thoroughly review the file then conduct detailed interviews. We have the ability to document statements through written, audio and/or video recording for legal proceedings. We also are able to provide transcribed reports with 48 hours of the interview. We are very flexible on the location of interviews, we understand that witness are sometimes not comfortable with an office setting so statements are frequently taken at the home of the interviewee.</p>
    </div>
    <div class="section" style="top:404px">
      <h2 class="section__title">Legal Testimony</h2>
      <p class="section__body">We recognize that legal testimony to support documented information is essential when hiring a private investigation firm. Our investigative personnel have trial experience and are fully prepared to testify at all legal proceedings.</p>
    </div>
    <div class="section" style="top:532px">
      <h2 class="section__title">Liability Investigations</h2>
      <p class="section__body">These investigations are typically related to automobile accidents, medical malpractice, product &amp; service liability, falling objects, motorcycles, and slip and fall. All finding are documented in a comprehensive report along with any evidence that was acquired during the investigation.</p>
    </div>
  </section>

  <section class="panel panel--middle">
    <div class="section" style="top:116px">
      <h2 class="section__title">Corporate Litigation</h2>
      <p class="section__body">Our investigators and researchers can perform a complete background or profile on all corporations involved in a specific litigated matter. Typically, a complete background on all principals and officers associated with the corporation is conducted. The focus of the investigation is tailored to each client's specific needs.</p>
    </div>
    <div class="section" style="top:276px">
      <h2 class="section__title">Domestic</h2>
      <p class="section__body">Infidelity, divorce and child custody investigations are tailored to the specific needs of the client and their attorney. We prefer to work directly for the attorney so that our findings are considered work product but you may refer your client directly to us if you choose.</p>
    </div>
    <div class="section" style="top:404px">
      <h2 class="section__title">Locates</h2>
      <p class="section__body">Our firm has located hundreds of people for a variety of reasons. Locating missing persons, heirs and witnesses are the most common reasons. We have the resources, ability and experience to find your witness and provide you with their current contact information. This can be accomplished on tight deadlines and within tight budgetary restraints.</p>
    </div>
    <div class="section" style="top:564px">
      <h2 class="section__title">Accident Reconstruction</h2>
      <p class="section__body">The investigation may include information and photographs from the scene through the development of witnesses, terrain, and other site conditions.</p>
    </div>
  </section>

  <section class="panel panel--right">
    <div class="section" style="top:116px">
      <h2 class="section__title">Competitive Intelligence</h2>
      <p class="section__body">In business, whoever has the best information wins. Brenwick Inquiry Partners strives to provide timely and accurate information which permits our clients to make better informed decisions, identify opportunities and compete more effectively. Our experience, which is rooted in conducting human intelligence collection, allows us to provide unique solutions for our clients. Our work includes:</p>
      <ul class="services">
        <li>Assisting with complex or difficult negotiations by identifying and filling information gaps.</li>
        <li>Examining risk and stability issues involving concerns over labor, local government, corruption and crime, physical security and regional security.</li>
        <li>Reporting on relevant aspects of supplier relationships or specific commodities that affect business operations, including productions levels, inventory, and shipping.</li>
        <li>Identify and counteract any rival effort to weaken the reputation of our client.</li>
        <li>Identify commercial and governmental allies of competitors while developing influential potential client contacts and relationships.</li>
      </ul>
    </div>
  </section>
</main>
</body>
</html>
```